How likely are people to engage in social distancing? We need a good illustration to show the data!

We surveyed U.S. adults March 20th - 24th, 2020 and asked how likely they were to engage in social distancing (and other COVID-19 related health behaviors). What did the survey find? Basically, most people intend to engage in social distancing behaviors (e.g., avoiding large crowds) and other behaviors that reduce the spread of COVID-19 (e.g., washing hands at least 20 seconds). When most people intend to engage in a behavior, then public health professionals try to leverage that to move more people to act.
Now we need innovative and professional images that attempt to communicate one or all of these findings. The specific findings are nicely summarized in the attached document. For example, 82% of participants intend to engage in social distancing.
What sort of visual are we looking for? Our preference is for an original illustration (or set of illustrations). Our preference is for (creative and powerful illustrations, but we are also open to the creative and well-executed infographics.
We need these images fast . We will award monetary prizes to the 3 best designs. If we like more than that, then we might purchase more (e.g., in past contests, we have purchased as many as 30 designs).
What we will need:
(1) The illustrations must be original and we will need the photoshop and/or illustrator files for all artwork.
(2) You can illustrate all of the findings or just one of them. We need creative approaches that do a lucid job of bringing the data to life. Most people intend to engage in these behaviors. How to communicate that? Corvantists and Halmerites do not differ in their intentions; how to communicate that?
(3) The illustration should say, somewhere: "Based on a survey of 400 U.S. adults conducted March 20 - 24th, 2020."

U.S. Adults

• Original illustrations based on the findings of the survey (see attached document).

```html
<!DOCTYPE html>
<html lang="en">
<head>
<meta charset="utf-8">
<title>Social Distancing Intentions</title>
<link href="https://fonts.googleapis.com/css2?family=Montserrat:wght@400;600;700&display=swap" rel="stylesheet">
<style>
  :root {
    --bg: #ffffff;
    --ink: #111111;
    --gold: #ffd000;
    --yellow: #fff200;
    --track: #777777;
    --red-a: #ff0000;
    --red-b: #d40000;
    --blue-a: #3a6fd2;
    --blue-b: #1a4fbd;
    --row-a: #ededed;
    --row-b: #dcdcdc;
    --red-head: #e60000;
    --blue-head: #2a62d0;
  }
  * { box-sizing: border-box; margin: 0; padding: 0; }
  html, body { width: 1200px; height: 1200px; overflow: hidden; background: var(--bg); }
  body { font-family: "Montserrat", Arial, sans-serif; color: var(--ink); position: relative; }

  .art { position: absolute; }
  .art-remote-work { left: 86px; top: 107px; width: 463px; height: 493px; }
  .art-hygiene { left: 771px; top: 493px; width: 360px; height: 617px; }

  .chart-title { position: absolute; left: 573px; top: 89px; font-size: 16px; font-weight: 700; white-space: nowrap; }

  .bar-list { position: absolute; left: 571px; top: 126px; width: 538px; list-style: none; }
  .bar { position: relative; height: 34px; margin-bottom: 7.5px; background: var(--track); }
  .bar-fill { position: absolute; left: 0; top: 0; bottom: 0; background: linear-gradient(90deg, var(--gold), var(--yellow) 70%); }
  .bar-label { position: absolute; left: 20px; top: 0; line-height: 34px; font-size: 16px; font-weight: 700; white-space: nowrap; }
  .bar-value { position: absolute; top: 0; line-height: 34px; font-size: 15px; font-weight: 700; color: #fff; padding-left: 12px; }

  .compare-title { position: absolute; left: 393px; top: 637px; font-size: 16px; font-weight: 700; white-space: nowrap; }
  .col-head { position: absolute; top: 672px; width: 132px; text-align: center; font-size: 18px; font-weight: 700; }
  .col-head.party-c { left: 469px; color: var(--red-head); }
  .col-head.party-h { left: 605px; color: var(--blue-head); }

  .compare-table { position: absolute; left: 92px; top: 711px; width: 645px; border-collapse: separate; border-spacing: 0; }
  .compare-table td { height: 42px; font-weight: 700; vertical-align: middle; }
  .compare-table .row-label { width: 372px; padding-left: 16px; font-size: 16px; line-height: 14px; background: var(--row-a); border-right: 4px solid #fff; }
  .compare-table .val { width: 132px; text-align: center; color: #fff; font-size: 17px; }
  .compare-table .val-c { background: var(--red-a); border-right: 4px solid #fff; }
  .compare-table .val-h { background: var(--blue-a); }
  .compare-table tr:nth-child(even) .row-label { background: var(--row-b); }
  .compare-table tr:nth-child(even) .val-c { background: var(--red-b); }
  .compare-table tr:nth-child(even) .val-h { background: var(--blue-b); }

  .source-note { position: absolute; left: 106px; top: 1068px; font-size: 11px; font-weight: 400; white-space: nowrap; }
</style>
</head>
<body>

<div class="art art-remote-work" role="img" aria-label="Illustration of a man on a phone call and a woman working on a laptop at home"
     style="background: radial-gradient(ellipse at 50% 25%, #f9d4d8 0%, #fbe3e5 40%, transparent 62%), radial-gradient(ellipse at 55% 75%, #c9e8f7 0%, #dff2fb 45%, transparent 68%);"></div>

<h1 class="chart-title">Percent of Americans intending to engage in social distancing</h1>
<ul class="bar-list">
  <li class="bar"><div class="bar-fill" style="width:82.5%"></div><span class="bar-label">Engage in social distancing</span><span class="bar-value" style="left:82.5%">82%</span></li>
  <li class="bar"><div class="bar-fill" style="width:63%"></div><span class="bar-label">Work from home</span><span class="bar-value" style="left:63%">63%</span></li>
  <li class="bar"><div class="bar-fill" style="width:85%"></div><span class="bar-label">Avoid large gatherings</span><span class="bar-value" style="left:85%">85%</span></li>
  <li class="bar"><div class="bar-fill" style="width:80.5%"></div><span class="bar-label">Cancel social activities</span><span class="bar-value" style="left:80.5%">81%</span></li>
  <li class="bar"><div class="bar-fill" style="width:85%"></div><span class="bar-label">Put distance between yourself and other people</span><span class="bar-value" style="left:85%">85%</span></li>
  <li class="bar"><div class="bar-fill" style="width:87.5%"></div><span class="bar-label">Wash hands at least 20 seconds</span><span class="bar-value" style="left:87.5%">87%</span></li>
  <li class="bar"><div class="bar-fill" style="width:85%"></div><span class="bar-label">Use hand sanitizer</span><span class="bar-value" style="left:85%">85%</span></li>
  <li class="bar"><div class="bar-fill" style="width:80.5%"></div><span class="bar-label">Avoid touching your eyes, nose, and mouth</span><span class="bar-value" style="left:80.5%">81%</span></li>
</ul>

<div class="art art-hygiene" role="img" aria-label="Illustration of a man wearing a face mask and a man washing his hands at a sink"
     style="background: radial-gradient(ellipse at 50% 30%, #d6f5c4 0%, #e6f9da 42%, transparent 64%), radial-gradient(ellipse at 50% 75%, #e4d2f5 0%, #efe3fa 45%, transparent 68%);"></div>

<h2 class="compare-title">Comparing Corvantists and Halmerites</h2>
<div class="col-head party-c">Corvantist</div>
<div class="col-head party-h">Halmerite</div>

<table class="compare-table">
  <tr><td class="row-label">Engage in social distancing</td><td class="val val-c">82%</td><td class="val val-h">81%</td></tr>
  <tr><td class="row-label">Work from home</td><td class="val val-c">60%</td><td class="val val-h">65%</td></tr>
  <tr><td class="row-label">Avoid large gatherings</td><td class="val val-c">85%</td><td class="val val-h">84%</td></tr>
  <tr><td class="row-label">Cancel social activities</td><td class="val val-c">82%</td><td class="val val-h">80%</td></tr>
  <tr><td class="row-label">Put distance between yourself and<br>other people</td><td class="val val-c">84%</td><td class="val val-h">87%</td></tr>
  <tr><td class="row-label">Wash hands at least 20 seconds</td><td class="val val-c">87%</td><td class="val val-h">88%</td></tr>
  <tr><td class="row-label">Use hand sanitizer</td><td class="val val-c">87%</td><td class="val val-h">84%</td></tr>
  <tr><td class="row-label">Avoid touching your eyes, nose<br>and mouth</td><td class="val val-c">80%</td><td class="val val-h">82%</td></tr>
</table>

<p class="source-note">Survey of U.S. Adults (N = 400) conducted March 20th - 24th, 2020</p>

</body>
</html>
```